Business card design needed

I am a nutritionist and fitness instructor and I need a business card designed for my company SowGrowThrive. I provide nutrition education services such as consultations, cooking demonstrations, workshops, and supermarket tours. I also provide fitness instruction and training to clients to help overhaul their lifestyle.

I would like to see designs that have a natural, organic, feel using earthy colours. I would like to have cards printed on recycled paper.

I would prefer a 2 sided card. Front side with just the business name Sow Grow Thrive and underneath Nutrition Health Fitness. The second side to have the contact details.

The final design should communicate health and wellness through eating organic wholefoods and being physically active.

Although I have this idea, I would be open to see other suggestions that have a similar look and feel.
Updates

Target Market(s)

people interested in being healthier, women wanting to loose weight, mothers wanting to be healthier for their families

Industry/Entity Type

Nutrition

Contact Information for Business Card

Nadia Crewe
Nutritionist and Personal Trainer
M 0417582936
E sowgrowthrivenutrition@mailbox-example.net

Logo Text

SowGrowThrive (underneath) Nutrition Health Fitness

Logo styles of interest
Wordmark Logo
Requirements
Nice to have
• I like the idea of having the letters of SowGrowThrive spelt out with food such as grains, nuts, seeds, legumes, fruit etc. For example close up images of cherry tomatoes, chia seeds, kidney beans, chickpeas, blue berries, raspberries, brown rice - lots of different colours and textures. Continuing playing on the idea of the book cover Dig Rest Glow.

food is important - I am not selling supplements rather I am promoting the enjoyment of healthy wholefoods so food is important to the look and feel of the design
Should not have
• cartoon images
images associated with body building or supplements
fruit or dumb bells with tape measures around them
clichés for weight loss such as scales and tape measures
I don't want to look like other typical wellness services such as massage or spa services

```html
<!DOCTYPE html>
<html lang="en">
<head>
<meta charset="utf-8">
<title>SowGrowThrive — Business Card</title>
<link rel="stylesheet" href="https://fonts.googleapis.com/css2?family=Arimo:wght@400;700&display=swap">
<style>
  :root{
    --stage:#ece8e1;
    --orange:#fb9b23;
    --orange-light:#ffc070;
    --green:#5fd11a;
    --green-light:#b6f04a;
    --lime-band:#dcf56a;
    --purple:#a21fe8;
    --wordmark:#3fae12;
    --shadow:rgba(60,40,20,.28);
  }
  *{margin:0;padding:0;box-sizing:border-box}
  html,body{width:1200px;height:1000px;overflow:hidden}
  body{background:var(--stage);font-family:"Arimo",Arial,sans-serif;position:relative}
  .card{position:absolute;top:350px;width:525px;height:300px;overflow:hidden;box-shadow:0 10px 28px var(--shadow)}
  .card--back{left:50px}
  .card--front{left:625px}
  .card svg{position:absolute;inset:0;width:100%;height:100%}

  .wordmark{position:absolute;font-weight:700;color:var(--wordmark);letter-spacing:.5px}
  .card--back .wordmark{top:18px;right:26px;font-size:20px}
  .identity{position:absolute;left:28px;top:98px}
  .identity__name{font-size:21px;color:var(--purple);letter-spacing:1px}
  .identity__role{font-size:9.5px;color:var(--purple);margin-top:8px;letter-spacing:.6px}
  .contact{position:absolute;left:24px;bottom:28px;list-style:none}
  .contact li{display:flex;align-items:center;gap:8px;font-size:15px;color:var(--purple);margin-top:8px}
  .contact svg{position:static;width:18px;height:18px}

  .card--front .wordmark{left:150px;top:110px;font-size:44px;letter-spacing:1px}
  .tagline{position:absolute;left:200px;top:163px;font-size:19px;color:var(--purple);letter-spacing:1px}
</style>
</head>
<body>

<section class="card card--back" aria-label="Business card, contact side">
  <svg viewBox="0 0 525 300" preserveAspectRatio="none">
    <defs>
      <linearGradient id="backGreen" x1="0" y1="0" x2="1" y2="1">
        <stop offset="0" stop-color="var(--green-light)"/>
        <stop offset="1" stop-color="var(--green)"/>
      </linearGradient>
      <linearGradient id="backOrange" x1="0" y1="0" x2="0" y2="1">
        <stop offset="0" stop-color="var(--orange-light)"/>
        <stop offset="1" stop-color="var(--orange)"/>
      </linearGradient>
    </defs>
    <rect class="card__base" width="525" height="300" fill="url(#backOrange)"/>
    <path class="card__green-field" d="M0 0H525V150Q262 300 0 150Z" fill="url(#backGreen)"/>
    <rect class="card__name-band" x="0" y="86" width="525" height="48" fill="var(--lime-band)" opacity=".75"/>
  </svg>
  <div class="wordmark">SowGrowThrive</div>
  <div class="identity">
    <div class="identity__name">Nadia Crewe</div>
    <div class="identity__role">Nutritionist and Personal Trainer</div>
  </div>
  <ul class="contact">
    <li>
      <svg viewBox="0 0 18 18" aria-hidden="true"><rect x="3" y="2" width="12" height="15" rx="2" fill="none" stroke="var(--purple)" stroke-width="1.6"/><rect x="5.5" y="4.5" width="7" height="3" fill="var(--purple)"/><g fill="var(--purple)"><circle cx="6.5" cy="10.5" r="1"/><circle cx="9" cy="10.5" r="1"/><circle cx="11.5" cy="10.5" r="1"/><circle cx="6.5" cy="13.5" r="1"/><circle cx="9" cy="13.5" r="1"/><circle cx="11.5" cy="13.5" r="1"/></g></svg>
      0417582936
    </li>
    <li>
      <svg viewBox="0 0 18 18" aria-hidden="true"><g fill="none" stroke="var(--purple)" stroke-width="1.4"><circle cx="9" cy="9" r="7"/><ellipse cx="9" cy="9" rx="3" ry="7"/><path d="M2 9H16M3.5 5H14.5M3.5 13H14.5"/></g></svg>
      sowgrowthrivenutrition@mailbox-example.net
    </li>
  </ul>
</section>

<section class="card card--front" aria-label="Business card, front side">
  <svg viewBox="0 0 525 300" preserveAspectRatio="none">
    <defs>
      <linearGradient id="frontGreen" x1="0" y1="0" x2="1" y2="1">
        <stop offset="0" stop-color="var(--green)"/>
        <stop offset="1" stop-color="var(--green-light)"/>
      </linearGradient>
      <radialGradient id="frontOrange" cx=".45" cy=".4" r=".7">
        <stop offset="0" stop-color="var(--orange-light)"/>
        <stop offset="1" stop-color="var(--orange)"/>
      </radialGradient>
    </defs>
    <rect class="card__base" width="525" height="300" fill="url(#frontGreen)"/>
    <rect class="card__produce-photo" x="200" y="180" width="325" height="120" fill="var(--green-light)" opacity=".45" role="img" aria-label="Photo of fresh green grapes"/>
    <path class="card__orange-field" d="M0 0H420Q440 230 0 255Z" fill="url(#frontOrange)"/>
    <ellipse class="card__active-photo" cx="230" cy="95" rx="140" ry="75" fill="#ffd29a" opacity=".45" role="img" aria-label="Faded photo of a woman stretching outdoors"/>
  </svg>
  <div class="wordmark">SowGrowThrive</div>
  <div class="tagline">Nutrition Health Fitness</div>
</section>

</body>
</html>
```